Graphic Design for Flavoured Drink product

I need a packaging design for flavoured drinks product.
The product is a mix of Sparkling Natural Mineral Water (from France) with other flavouring.

There will be various flavours i.e. apple, orange, strawberry, etc.
However, you may design the product using one sample flavour first, as the designs of other flavours could be adjusted afterwards.

The temporary product name is: QUIVLO

I want the product design to be something 'fun' and 'colourful'.
The design concept could be anything depends on your imagination.
Basically, I want you to be creative in designing the logo and the overall graphic design for the label.

- Create something different. Something extraordinary -

Thank you and Good Luck!

Additional:

The measurement is 20cm (Length) x 10cm (Height).

The target customers are young audiences (10 years - 35 years old).

I am hoping to have a product design that can stand out in the supermarket shelf.
It must be eye catchy and attractive.

Thank you,
Marcus

-PLEASE REFER TO DESIGN SAMPLE ATTACHED TO HAVE A BETTER UNDERSTANDING FOR THE PRODUCT CONCEPT-

Reason: I havent found any satisfactory designs so far. Please submit much better quality designs. Thank you, Marcus

```html
<!DOCTYPE html>
<html lang="en">
<head>
<meta charset="utf-8">
<title>QUIVLO – Sparkling Orange Label</title>
<link href="https://fonts.googleapis.com/css2?family=Cabin:wght@400;600;700&family=Kalam:wght@700&display=swap" rel="stylesheet">
<style>
  :root {
    --page: #e9eaea;
    --label-top: #cfd8de;
    --label-mid: #e4e9ec;
    --label-bottom: #f1f3f4;
    --logo: #f0a92a;
    --band: #8a3fb0;
    --band-text: #ffffff;
    --tag: #f7e43a;
    --tag-text: #5a4a10;
    --body-text: #3c4654;
    --juice-light: #f6c64a;
    --juice-deep: #e99a25;
    --slice: #f4a53a;
    --slice-deep: #e07d1f;
  }
  html, body {
    margin: 0;
    padding: 0;
    width: 1200px;
    height: 1000px;
    overflow: hidden;
    background: var(--page);
  }
  .canvas {
    position: relative;
    width: 1200px;
    height: 1000px;
  }
  .label {
    position: absolute;
    left: 60px;
    top: 220px;
    width: 1080px;
    height: 540px;
    overflow: hidden;
    background: linear-gradient(180deg, var(--label-top) 0%, var(--label-mid) 45%, var(--label-bottom) 100%);
    box-shadow: 0 6px 24px rgba(0,0,0,0.12);
    font-family: "Cabin", sans-serif;
  }
  .juice-band {
    position: absolute;
    left: 0;
    bottom: 0;
    width: 1080px;
    height: 210px;
  }
  .brand {
    position: absolute;
    left: 60px;
    top: 40px;
    margin: 0;
    font-family: "Cabin", sans-serif;
    font-weight: 700;
    font-size: 104px;
    letter-spacing: 4px;
    line-height: 1;
    color: var(--logo);
  }
  .descriptor {
    position: absolute;
    left: 60px;
    top: 160px;
    padding: 8px 22px;
    background: var(--band);
    color: var(--band-text);
    font-variant: small-caps;
    font-weight: 600;
    font-size: 24px;
    letter-spacing: 1px;
    border-radius: 4px;
  }
  .vitamin-tag {
    position: absolute;
    left: 420px;
    top: 222px;
    padding: 4px 18px;
    background: var(--tag);
    color: var(--tag-text);
    font-family: "Kalam", cursive;
    font-size: 28px;
    transform: rotate(-6deg);
    box-shadow: 0 2px 4px rgba(0,0,0,0.15);
  }
  .benefits {
    position: absolute;
    left: 60px;
    top: 250px;
    margin: 0;
    padding: 0;
    list-style: none;
    color: var(--body-text);
    font-size: 22px;
    line-height: 1.55;
  }
  .benefits li::before {
    content: "•";
    margin-right: 10px;
    color: var(--slice-deep);
  }
  .fruit-art {
    position: absolute;
    left: 650px;
    top: 120px;
    width: 300px;
    height: 300px;
  }
  .volume {
    position: absolute;
    right: 60px;
    bottom: 30px;
    color: #ffffff;
    font-weight: 600;
    font-size: 22px;
    letter-spacing: 1px;
  }
</style>
</head>
<body>
  <main class="canvas">
    <section class="label">
      <svg class="juice-band" viewBox="0 0 1080 210" preserveAspectRatio="none" aria-hidden="true">
        <defs>
          <linearGradient id="juiceFill" x1="0" y1="0" x2="0" y2="1">
            <stop offset="0" stop-color="var(--juice-light)"/>
            <stop offset="1" stop-color="var(--juice-deep)"/>
          </linearGradient>
        </defs>
        <path d="M0 40 C 180 10, 360 70, 540 40 S 900 10, 1080 45 L1080 210 L0 210 Z" fill="url(#juiceFill)"/>
      </svg>

      <h1 class="brand">QUIVLO</h1>
      <div class="descriptor">Juice Infused Sparkling Mineral Water</div>
      <div class="vitamin-tag">Vitamins A &amp; C</div>

      <ul class="benefits">
        <li>Low Calorie</li>
        <li>Sparkling Mineral Water from France</li>
        <li>High in Vitamins A &amp; C</li>
      </ul>

      <svg class="fruit-art" viewBox="0 0 300 300" role="img" aria-label="Illustration of a halved orange slice splashing into orange juice">
        <defs>
          <radialGradient id="sliceFill" cx="0.5" cy="0.5" r="0.5">
            <stop offset="0" stop-color="#fbd48a"/>
            <stop offset="0.8" stop-color="var(--slice)"/>
            <stop offset="1" stop-color="var(--slice-deep)"/>
          </radialGradient>
        </defs>
        <circle cx="150" cy="150" r="140" fill="url(#sliceFill)"/>
      </svg>

      <div class="volume">8 fl. oz</div>
    </section>
  </main>
</body>
</html>
```